Flyer for a Business Consultant

I need a one-page description of services. I am a Brinmore Accredited Talents Mentor. I do not have a personal website but think I will soon purchase this template https://quillerlayouts.example/layouts/lectern/. I like the larger font, simplicity and larger font. I will attach his pricing flyer which I like - not to overly guide or restrict your creative thinking, but only to give a little perspective. I don't like busy, noisy - I like clarity, simplicity. Here 's the Brinmore website which these same traits https://www.brinmoretalentshub.example/ and can be a source of ideas and colors.

Target Market(s)

CEOs and Middle Managers in organizations

Industry/Entity Type

Financial Service

Colors

Designer to choose colors to be used in the design.

Requirements
Must have
• Clarity, simplicity, but also strength (not weak or frilly looking)
Nice to have
• Warm color(s), larger/not skinny font
Should not have
• Loud, noisy, busy

```html
<!DOCTYPE html>
<html lang="en">
<head>
<meta charset="utf-8">
<title>Brinmore Accredited Talents Mentor – Services Flyer</title>
<link rel="stylesheet" href="https://fonts.googleapis.com/css2?family=Raleway:wght@500;600;700;800&family=Lora:ital,wght@1,700&display=swap">
<style>
  :root {
    --stage: #d9d9d9;
    --paper: #f4f4f4;
    --paper-edge: #e8e8e8;
    --brand-blue: #1b75bb;
    --banner-top: #1f6fbf;
    --banner-bottom: #4a8fd2;
    --text-grey: #5a5a5a;
    --logo-grey: #777777;
    --rule-grey: #9a9a9a;
    --white: #ffffff;
  }
  * { box-sizing: border-box; margin: 0; padding: 0; }
  html, body { width: 1200px; height: 834px; overflow: hidden; }
  body {
    background: var(--stage);
    font-family: "Raleway", Arial, sans-serif;
    position: relative;
  }
  .flyer {
    position: absolute;
    left: 300px; top: 17px;
    width: 600px; height: 800px;
    background: radial-gradient(ellipse at 50% 40%, var(--paper) 60%, var(--paper-edge) 100%);
    padding: 30px 40px 0;
    box-shadow: 0 2px 10px rgba(0,0,0,.2);
  }
  .masthead { display: flex; align-items: center; height: 82px; }
  .credential {
    width: 276px; height: 78px;
    border: 1px solid #a8a8a8;
    margin-left: 14px;
    display: flex; align-items: center; gap: 12px;
    padding: 0 14px;
  }
  .credential-mark { width: 32px; height: 32px; background: var(--logo-grey); flex: none; }
  .credential-name { color: var(--logo-grey); font-weight: 600; font-size: 15px; line-height: 1.3; }
  .contact {
    margin-left: 48px;
    border-left: 2px solid var(--brand-blue);
    padding-left: 10px;
    color: var(--brand-blue);
    font-weight: 700; font-size: 11.5px; line-height: 20px;
  }
  .contact-row { display: flex; align-items: center; gap: 12px; }
  .contact-row svg { width: 14px; height: 12px; flex: none; }

  .banner {
    margin-top: 26px;
    height: 266px;
    background: linear-gradient(180deg, var(--banner-top), var(--banner-bottom));
    color: var(--white);
    padding: 22px 38px 0;
  }
  .banner-title { font-weight: 800; font-size: 26px; line-height: 38px; text-align: center; }
  .banner-lead { font-family: "Lora", Georgia, serif; font-style: italic; font-weight: 700; font-size: 15px; text-align: center; margin: 2px 0 14px; }
  .benefits { list-style: none; }
  .benefits li {
    border-left: 7px solid var(--white);
    padding-left: 10px;
    font-weight: 700; font-size: 13px; line-height: 18px;
    margin-bottom: 14px;
  }

  .service { padding: 22px 0 14px; border-bottom: 1.5px dashed var(--rule-grey); }
  .service:last-child { border-bottom: none; }
  .service-title { color: var(--brand-blue); font-weight: 800; font-size: 17px; margin-bottom: 4px; }
  .service-body { display: flex; gap: 24px; }
  .service-icon { width: 62px; height: 56px; flex: none; display: flex; justify-content: center; }
  .service-icon span { display: block; width: 44px; height: 50px; background: var(--brand-blue); border-radius: 6px; }
  .service-text { color: var(--text-grey); font-weight: 600; font-size: 10.8px; line-height: 16.5px; text-align: justify; }
</style>
</head>
<body>
  <article class="flyer">
    <header class="masthead">
      <div class="credential">
        <span class="credential-mark"></span>
        <span class="credential-name">Brinmore Accredited<br>Talents Mentor</span>
      </div>
      <div class="contact">
        <div>Warren Calloway</div>
        <div>Brinmore Workplace Talents Mentor</div>
        <div class="contact-row">
          <svg viewBox="0 0 14 12" aria-hidden="true"><rect x="1" y="1" width="12" height="10" fill="none" stroke="currentColor" stroke-width="1.6"/><path d="M1 1 L7 6.5 L13 1" fill="none" stroke="currentColor" stroke-width="1.6"/></svg>
          <span>warren@talentsguide.example</span>
        </div>
        <div class="contact-row">
          <svg viewBox="0 0 14 12" aria-hidden="true"><path d="M3 0.5 L5.5 2.8 L4.2 4.6 Q5.5 7.5 8 8.8 L9.6 7.4 L12 9.8 L10.3 11.5 Q3.5 10.5 1.3 2.2 Z" fill="currentColor"/></svg>
          <span>555-014-2273</span>
        </div>
      </div>
    </header>

    <section class="banner">
      <h1 class="banner-title">A Strength-based Approach to<br>Managing Team Effectiveness</h1>
      <p class="banner-lead">We help teams grow stronger by:</p>
      <ul class="benefits">
        <li>Bringing a deep awareness of their strengths and the strengths of their associates.</li>
        <li>Increasing the Team’s communication and sense of partnership.</li>
        <li>Improving employee engagement and effectiveness.</li>
      </ul>
    </section>

    <section class="service">
      <h2 class="service-title">Individual sessions</h2>
      <div class="service-body">
        <div class="service-icon"><span role="img" aria-label="Icon of a coach standing"></span></div>
        <p class="service-text">Conversational feedback and coaching sessions based on KeystoneTalents assessments. These sessions last about an hour and lead to a personalized translation of the results and how their strengths show up in their work and inherent blind spots they bring.</p>
      </div>
    </section>

    <section class="service">
      <h2 class="service-title">Strength Discovery Workshop</h2>
      <div class="service-body">
        <div class="service-icon"><span role="img" aria-label="Icon of a head with a glowing brain"></span></div>
        <p class="service-text">A retreat-style Team Workshop in which the team learns each other’s unique Top 5 strengths. The session is very interactive and provides a common language that leads to improved communication and effectiveness. Tailored in 2.3.and 4-hour options are tailored to your Team’s challenges and opportunities.</p>
      </div>
    </section>

    <section class="service">
      <h2 class="service-title">Follow-on modules</h2>
      <div class="service-body">
        <div class="service-icon"><span role="img" aria-label="Icon of stacked building blocks"></span></div>
        <p class="service-text">Follow-on is important to make the insights learned to be practical and integrated into the Teams’ approach and workflows. In a debrief session included as part of the workshop, we provide several 15-minute exercise modules for use in regular meetings, and we offer guest facilitated modules of 30- 60 minutes each.</p>
      </div>
    </section>
  </article>
</body>
</html>
```